VineGlow Artbook for Okanagan Region, British Columbia

Creating an art book: VineGlow, for the Okanagan Wine Region in British Columbia, Canada. Would like smart, modern, clean and linear...cool, sexy urban, not ugly boring suburban... I need a cover that appeals to the wino in all of us! Title: VineGlow -Marla Pettivan
Updates
Thank you all kindly for your efforts. I have added some files so that you can get a sense of my aesthetic...it's never easy trying to figure it out, is it? I will hopefully have dimensions of book soon...cheers, Marla
would anyone please design a giant wine bottle with the wine label that looks like a label but says vineglow...just curious to see if it works as a design or not...thank you.
Target Market(s)
Designing this wine art book of quotes to wineries in Okanagan BC. Buyer is wine lover and tourist ready to spend his vacation bucks on this wonderful book!
Look and feel

```html
<!DOCTYPE html>
<html lang="en">
<head>
<meta charset="utf-8">
<title>VineGlow — Book Cover</title>
<link rel="stylesheet" href="https://fonts.googleapis.com/css2?family=Arimo:wght@400;700&display=swap">
<style>
  :root {
    --page-bg: #ffffff;
    --cork-light: #d9b48a;
    --cork-mid: #c39063;
    --cork-rose: #b97a6e;
    --cork-dark: #7a5236;
    --label-top: #ffffff;
    --label-bottom: #e4e4e4;
    --title-red: #d01f2c;
    --byline-grey: #6e6e6e;
  }

  html, body {
    margin: 0;
    padding: 0;
    width: 1200px;
    height: 907px;
    overflow: hidden;
    background: var(--page-bg);
  }

  .canvas {
    position: relative;
    width: 1200px;
    height: 907px;
  }

  .book-cover {
    position: absolute;
    left: 377px;
    top: 88px;
    width: 446px;
    height: 731px;
    overflow: hidden;
    box-shadow: 0 6px 24px rgba(0, 0, 0, 0.18);
  }

  .cork-photo {
    position: absolute;
    inset: 0;
    background:
      repeating-linear-gradient(90deg, rgba(80, 50, 30, 0.25) 0 3px, transparent 3px 48px),
      repeating-linear-gradient(0deg, rgba(60, 35, 20, 0.35) 0 4px, transparent 4px 104px),
      linear-gradient(160deg, var(--cork-light) 0%, var(--cork-mid) 35%, var(--cork-rose) 60%, var(--cork-mid) 80%, var(--cork-dark) 100%);
  }

  .title-label {
    position: absolute;
    left: 140px;
    top: 192px;
    right: 0;
    height: 114px;
    background: var(--label-top);
    box-shadow: -2px 3px 8px rgba(0, 0, 0, 0.25);
    font-family: "Arimo", Arial, sans-serif;
  }

  .title {
    margin: 0;
    height: 72px;
    display: flex;
    align-items: center;
    padding-left: 22px;
    font-size: 50px;
    font-weight: 700;
    letter-spacing: -1px;
    color: var(--title-red);
    transform: scaleX(0.92);
    transform-origin: left center;
  }

  .byline {
    margin: 0;
    height: 42px;
    line-height: 40px;
    padding-left: 26px;
    background: var(--label-bottom);
    font-size: 21px;
    font-weight: 400;
    letter-spacing: 1.5px;
    color: var(--byline-grey);
  }
</style>
</head>
<body>
  <main class="canvas">
    <section class="book-cover">
      <div class="cork-photo" role="img" aria-label="Photograph of stacked wine corks with stamped winery markings filling the cover"></div>
      <div class="title-label">
        <h1 class="title">VineGlow</h1>
        <p class="byline">by Marla Pettivan</p>
      </div>
    </section>
  </main>
</body>
</html>
```